Flyer for Brightwell Table Provisions Company

Flyer Size: Double Sided 210mm * 148mm (Half a Sheet of Paper)
For your reference I have attached the logo and the web address is www.brightwelltableprovisions.com.
Specifications:
- Must contain the menu pricing chart, contact information, and hours of operation posted on the website.
- The menu must have an organization system from 1. Select Glaze through 4.Drinks. This will be the determining factor for selection. Graphic must be a mixture of creativity and function.
-The flyer can be identical on both sides (Not a determining factor)
-Incorporate the logo on both sides.
-The flyer does not have to be based on the website. (Not a determining factor)
My team will be handing these flyers out to HR Directors and Securities at Corporate offices.
Please let me know if you have any questions.
Updates
Project Deadline Extended
Reason: Website was not operational .
Brief has been updated and the website is up for your reference.
Target Market(s)
Corporate Office Catering. Secretary or HR director, usually a female.
Industry/Entity Type
Catering
Look and feel

```html
<!DOCTYPE html>
<html lang="en">
<head>
<meta charset="utf-8">
<title>Brightwell Table Provisions – Catering Flyer</title>
<link href="https://fonts.googleapis.com/css2?family=Original+Surfer&family=Andika:wght@400;700&display=swap" rel="stylesheet">
<style>
  :root{
    --backdrop:#e9e9e9;
    --card:#ffffff;
    --card-tint:#f1f1f1;
    --orange:#f46a2b;
    --orange-deep:#e8322a;
    --ring:#b5222a;
    --ink:#505050;
    --ink-soft:#5a5a5a;
    --red-text:#a3161c;
    --white:#ffffff;
  }
  *{box-sizing:border-box;margin:0;padding:0}
  html,body{width:1200px;height:900px;overflow:hidden}
  body{background:var(--backdrop);position:relative;font-family:"Andika",sans-serif}
  .flyer{position:absolute;top:135px;width:448px;height:630px;background:var(--card);box-shadow:0 2px 8px rgba(0,0,0,.18);overflow:hidden}
  .flyer--menu{left:102px}
  .flyer--info{left:651px}
  .flyer__pattern{position:absolute;inset:0;background:radial-gradient(circle at 50% 55%,var(--card) 0%,var(--card-tint) 100%)}
  .brand{position:absolute;top:38px;left:0;width:100%;display:flex;justify-content:center;align-items:center;gap:12px}
  .brand__dot{width:58px;height:58px;border-radius:50%;background:var(--orange)}
  .brand__name{font-family:"Andika",sans-serif;font-weight:700;font-size:21px;line-height:1.05;color:var(--orange)}
  .menu-art{position:absolute;left:0;top:0}
  .label{position:absolute;font-family:"Original Surfer",sans-serif;font-weight:400;color:var(--ink);text-align:center;line-height:1;text-transform:uppercase}
  .label--glaze{left:16px;top:158px;width:120px;font-size:16px}
  .label--sides{left:311px;top:152px;width:90px;font-size:19px}
  .label--dessert{left:120px;top:422px;width:76px;font-size:14px}
  .label--drinks{left:315px;top:480px;width:116px;font-size:22px}
  .list{position:absolute;list-style:none;font-family:"Andika",sans-serif;color:var(--white);font-size:9px;line-height:14.4px;text-transform:uppercase;letter-spacing:.3px;white-space:nowrap}
  .list--glaze-a{left:68px;top:256px}
  .list--glaze-b{left:134px;top:223px}
  .list--sides{left:273px;top:223px}
  .list--drinks{left:235px;top:370px}
  .list--dessert{left:61px;top:496px}
  .hours{position:absolute;top:152px;left:0;width:100%;text-align:center}
  .hours__title{font-family:"Original Surfer",sans-serif;font-size:29px;color:var(--ink);font-weight:400;text-transform:uppercase;white-space:nowrap}
  .hours__line{font-family:"Original Surfer",sans-serif;font-size:14px;color:var(--red-text);margin-top:12px;text-transform:uppercase}
  .price-box{position:absolute;left:27px;top:306px;width:394px;height:192px;border-radius:8px;border:4px solid #d0d0d0;background:linear-gradient(var(--orange),var(--orange-deep));color:var(--white);text-align:center}
  .price-box__title{font-family:"Original Surfer",sans-serif;font-weight:400;font-size:35px;margin-top:24px;line-height:1}
  .price-box__sub{font-family:"Original Surfer",sans-serif;font-size:17px;margin-top:6px}
  .price-box__rule{width:276px;height:2px;background:var(--white);margin:20px auto 0}
  .price-table{position:absolute;left:6px;top:130px;width:376px;border-collapse:collapse;font-weight:700;font-size:9.5px}
  .price-table th{text-align:left;font-weight:700;padding:5px 0;width:74px}
  .price-table td{text-align:center;padding:5px 0}
  .contact{position:absolute;top:540px;left:0;width:100%;text-align:center;font-family:"Original Surfer",sans-serif;color:var(--ink-soft);line-height:28px;white-space:nowrap}
  .contact__phone{font-size:21px}
  .contact__email{text-transform:uppercase;font-size:16px}
</style>
</head>
<body>

<section class="flyer flyer--menu">
  <div class="flyer__pattern" role="img" aria-label="Soft grey paisley pattern background"></div>
  <div class="brand">
    <span class="brand__dot"></span>
    <span class="brand__name">Brightwell Table<br>Provisions</span>
  </div>

  <svg class="menu-art" width="448" height="630" viewBox="0 0 448 630" aria-hidden="true">
    <defs>
      <linearGradient id="orangeFill" x1="0" y1="0" x2="0" y2="1">
        <stop offset="0" stop-color="#f46a2b"/>
        <stop offset="1" stop-color="#e8322a"/>
      </linearGradient>
      <radialGradient id="labelFill" cx="0.4" cy="0.35" r="0.7">
        <stop offset="0.6" stop-color="#ffffff"/>
        <stop offset="1" stop-color="#d9d9d9"/>
      </radialGradient>
      <filter id="soft" x="-30%" y="-30%" width="160%" height="160%">
        <feDropShadow dx="0" dy="2" stdDeviation="4" flood-opacity=".3"/>
      </filter>
    </defs>
    <g stroke="#b5222a" stroke-width="6" fill="url(#orangeFill)">
      <circle cx="150" cy="300" r="120"/>
      <circle cx="118" cy="507" r="80"/>
      <circle cx="298" cy="426" r="100"/>
      <circle cx="326" cy="262" r="84"/>
    </g>
    <g fill="url(#labelFill)" filter="url(#soft)">
      <circle cx="76" cy="195" r="62"/>
      <circle cx="356" cy="170" r="47"/>
      <circle cx="158" cy="443" r="40"/>
      <circle cx="373" cy="505" r="58"/>
    </g>
  </svg>

  <h2 class="label label--glaze">Select Rotisserie Chicken Glaze</h2>
  <h2 class="label label--sides">Select Sides</h2>
  <h2 class="label label--dessert">Select Dessert</h2>
  <h2 class="label label--drinks">Select Drinks</h2>

  <ul class="list list--glaze-a">
    <li>Original</li><li>Barbecue</li><li>Honey</li><li>Spicy</li><li>Chipotle</li><li>Chipotle-Lime</li><li>Jamaican Jerk</li><li>Teriyaki</li><li>Buffalo</li>
  </ul>
  <ul class="list list--glaze-b">
    <li>Balsamic Chicken</li><li>Hawaiian</li><li>Lemon Pepper Rosema</li><li>Lemonade Chicken</li><li>Lemon Zest</li><li>Orange</li><li>Orange and Onion</li>
  </ul>
  <ul class="list list--sides">
    <li>Balsamic Chicken</li><li>Hawaiian</li><li>Lemon Pepper Rosemary</li><li>Lemonade Chicken</li><li>Lemon Zest</li><li>Orange</li><li>Orange and Onion</li>
  </ul>
  <ul class="list list--drinks">
    <li>Redcap Cola</li><li>Bluecrest Cola</li><li>Limelight Soda</li><li>Desert Bloom Ice Tea</li><li>(Iced Tea &amp; Lemon Tea)</li><li>Stillbrook Water</li>
  </ul>
  <ul class="list list--dessert">
    <li>Nuttina Covered</li><li>Chocolate Chip Cookies</li>
  </ul>
</section>

<section class="flyer flyer--info">
  <div class="flyer__pattern" role="img" aria-label="Soft grey paisley pattern background"></div>
  <div class="brand">
    <span class="brand__dot"></span>
    <span class="brand__name">Brightwell Table<br>Provisions</span>
  </div>

  <div class="hours">
    <h2 class="hours__title">Hours of Operation:</h2>
    <p class="hours__line">Monday - Saturday 8 AM-10 PM</p>
    <p class="hours__line">Sunday 8 AM -8 PM</p>
  </div>

  <div class="price-box">
    <h2 class="price-box__title">AVERAGE PRICE</h2>
    <p class="price-box__sub">(with delivery and sides)</p>
    <div class="price-box__rule"></div>
    <table class="price-table">
      <tr><th>PARTY SIZE:</th><td>10</td><td>20</td><td>30</td><td>40</td><td>50</td><td>60</td><td>80</td><td>100</td><td>150</td><td>200</td></tr>
      <tr><th>PRICE:</th><td>$105</td><td>$165</td><td>$225</td><td>$290</td><td>$330</td><td>$395</td><td>$515</td><td>$625</td><td>$940</td><td>$1,235</td></tr>
    </table>
  </div>

  <div class="contact">
    <p class="contact__phone">(555) 214-7730</p>
    <p class="contact__email">sales@brightwelltableprovisions.com</p>
  </div>
</section>

</body>
</html>
```